Construction Company

Design a clutter free business card, it can be double-sided utilizing the logo for BDN Ltd simple with all relevant contact information.

Please also a letterhead design to function for the purposes of invoicing, all mail requirements, with header to be distinctive while the footer ties page together and incorporates all necessary information.

For now, please use generic / dummy text and when a winner is selected, I will disclose the contact information.

Hi Designers! Please read the updated brief which includes the design of a business card and letterhead. Thank you!

```html
<!DOCTYPE html>
<html lang="en">
<head>
<meta charset="UTF-8">
<title>BDN Ltd — Business Card</title>
<link href="https://fonts.googleapis.com/css2?family=Poppins:wght@400;500;600&display=swap" rel="stylesheet">
<style>
  :root {
    --stage: #1c1c1e;
    --navy: #0b2a9c;
    --royal: #0a2fa8;
    --royal-light: #1446d6;
    --gold: #b8901e;
    --ink: #4a4a52;
    --paper: #ffffff;
  }
  * { margin: 0; padding: 0; box-sizing: border-box; }
  html, body {
    width: 1200px; height: 800px; overflow: hidden;
    background: var(--stage);
    font-family: "Poppins", sans-serif;
  }
  .stage {
    width: 1200px; height: 800px;
    display: flex; align-items: center; justify-content: center; gap: 40px;
  }
  .card {
    width: 540px; height: 310px;
    border-radius: 22px;
    position: relative;
    overflow: hidden;
  }
  .card-back {
    background: linear-gradient(120deg, var(--royal-light) 0%, var(--royal) 45%, #07227f 100%);
  }
  .card-front {
    background: var(--paper);
    padding: 40px 36px;
    display: flex; justify-content: space-between; align-items: center;
  }
  .contact { display: flex; flex-direction: column; }
  .contact-name {
    color: var(--navy); font-weight: 600; font-size: 18px;
    text-transform: uppercase; letter-spacing: 0.2px; line-height: 1.1;
  }
  .contact-role { color: var(--gold); font-size: 12px; margin-top: 2px; }
  .contact-email { color: var(--ink); font-size: 11.5px; letter-spacing: 0.6px; margin-top: 2px; }
  .divider {
    width: 62px; border-top: 2px dotted var(--navy);
    margin: 16px 0 14px 8px;
  }
  .phones { list-style: none; font-size: 11.5px; color: var(--ink); line-height: 1.45; padding-left: 8px; }
  .phones .label { color: var(--navy); font-weight: 500; }
  .address { font-size: 11.5px; color: var(--ink); line-height: 1.4; padding-left: 8px; }
  .website {
    font-size: 12px; letter-spacing: 3px; margin-top: 6px; padding-left: 8px;
    color: var(--navy);
  }
  .website .domain { color: var(--gold); }
  .brand {
    display: flex; align-items: center; gap: 10px;
    margin-right: 20px; margin-top: -30px;
  }
  .brand-dot { width: 16px; height: 16px; border-radius: 50%; background: var(--gold); }
  .brand-name { color: var(--navy); font-weight: 600; font-size: 40px; letter-spacing: 0.5px; }
</style>
</head>
<body>
  <main class="stage">
    <section class="card card-back" role="img" aria-label="Card back: repeating outline flower pattern on royal blue"></section>

    <section class="card card-front">
      <div class="contact">
        <h1 class="contact-name">Daniel Harper</h1>
        <p class="contact-role">President</p>
        <p class="contact-email">info@bdnltd.com</p>
        <div class="divider"></div>
        <ul class="phones">
          <li><span class="label">Tel .</span> 555-214-7730</li>
          <li><span class="label">Mob .</span> 555-318-4062</li>
          <li><span class="label">Fax .</span> 555-427-1195</li>
        </ul>
        <div class="divider"></div>
        <p class="address">2140 Cedar Ridge Road<br>Fairview, Oregon 97024</p>
        <p class="website">WWW.<span class="domain">BDNLTD</span>.COM</p>
      </div>
      <div class="brand">
        <span class="brand-dot"></span>
        <span class="brand-name">BDN Ltd</span>
      </div>
    </section>
  </main>
</body>
</html>
```